Kelmora Legal Business Card

I require a corporate business card for a new legal services business.

I do not have a logo, nor do I want one.

I require a clean, neat a professional card for a law firm.

Details:

Business Name: Kelmora Legal
Name: Debra Lindqvist
Title: Corporate Services Manager
Location: Office 14 (Top Floor), Toravel Business Centre, Quinlan Grove Street, Alotau CBD, Milne Bay Province.
Postal Address: PO Box 593, Alotau, 211, Milne Bay Province, Papua New Guinea.
Contact: T: +675 6418250, F: +675 6413362, M: +675 72915867, E: dlindqvist@kelmoraexample.com.pg.

I look forward to your design submissions.

Industry/Entity Type

Legal

```html
<!DOCTYPE html>
<html lang="en">
<head>
<meta charset="utf-8">
<title>Kelmora Legal – Business Card</title>
<link rel="stylesheet" href="https://fonts.googleapis.com/css2?family=Source+Sans+3:wght@300;400;600;700&display=swap">
<style>
  :root {
    --backdrop: #e4e4e2;
    --card-top: #ffffff;
    --card-bottom: #e7e8ea;
    --navy: #1e3877;
    --navy-deep: #152a5e;
    --accent-blue: #2f56a6;
    --ink: #2a2a2a;
    --ink-soft: #555a62;
    --rule: #1c1c1c;
    --band-text: #ffffff;
  }
  html, body {
    margin: 0;
    width: 1200px;
    height: 1023px;
    overflow: hidden;
    background: var(--backdrop);
    font-family: "Source Sans 3", "Myriad Pro", sans-serif;
  }
  .card {
    position: absolute;
    left: 100px;
    top: 225px;
    width: 1000px;
    height: 572px;
    border-radius: 26px;
    overflow: hidden;
    background: linear-gradient(160deg, var(--card-top) 0%, #f3f4f5 55%, var(--card-bottom) 100%);
    box-shadow: 0 18px 40px rgba(0,0,0,0.22), 0 2px 6px rgba(0,0,0,0.12);
  }
  .wordmark {
    position: absolute;
    left: 70px;
    top: 190px;
    margin: 0;
    font-size: 76px;
    font-weight: 600;
    line-height: 1;
    letter-spacing: -1px;
    color: var(--navy);
  }
  .header-rule {
    position: absolute;
    left: 560px;
    top: 246px;
    width: 370px;
    height: 2px;
    background: var(--rule);
  }
  .office-address {
    position: absolute;
    right: 70px;
    top: 62px;
    margin: 0;
    text-align: right;
    font-style: normal;
    font-size: 25px;
    font-weight: 600;
    line-height: 1.3;
    color: var(--ink);
  }
  .person {
    position: absolute;
    left: 72px;
    top: 280px;
  }
  .person-name {
    margin: 0;
    font-size: 32px;
    font-weight: 600;
    line-height: 1.05;
    color: var(--accent-blue);
  }
  .person-title {
    margin: 0;
    font-size: 25px;
    font-weight: 400;
    line-height: 1.2;
    color: var(--ink);
  }
  .name-rule {
    width: 250px;
    height: 2px;
    margin-top: 10px;
    background: var(--rule);
  }
  .contact-list {
    position: absolute;
    left: 72px;
    top: 370px;
    margin: 0;
    padding: 0;
    list-style: none;
    font-size: 21px;
    line-height: 1.22;
    color: var(--ink-soft);
  }
  .contact-label {
    color: var(--accent-blue);
    font-weight: 600;
    margin-right: 6px;
  }
  .postal-band {
    position: absolute;
    left: 0;
    right: 0;
    bottom: 0;
    height: 78px;
    background: linear-gradient(180deg, var(--navy) 0%, var(--navy-deep) 100%);
    display: flex;
    align-items: center;
    justify-content: flex-end;
    padding-right: 58px;
    box-sizing: border-box;
  }
  .postal-address {
    margin: 0;
    font-style: normal;
    font-size: 25px;
    font-weight: 400;
    color: var(--band-text);
  }
</style>
</head>
<body>
  <article class="card">
    <address class="office-address">
      Office 14 (Top Floor)<br>
      Toravel Business Centre<br>
      Quinlan Grove Street, Alotau CBD<br>
      Milne Bay Province
    </address>

    <h1 class="wordmark">Kelmora Legal</h1>
    <div class="header-rule"></div>

    <div class="person">
      <p class="person-name">Debra Lindqvist</p>
      <p class="person-title">Corporate Services Manager</p>
      <div class="name-rule"></div>
    </div>

    <ul class="contact-list">
      <li><span class="contact-label">T:</span>+675 6418250</li>
      <li><span class="contact-label">F:</span>+675 6413362</li>
      <li><span class="contact-label">M:</span>+675 72915867</li>
      <li><span class="contact-label">E:</span>dlindqvist@kelmoraexample.com.pg</li>
    </ul>

    <footer class="postal-band">
      <address class="postal-address">PO Box 593, Alotau, 211, Milne Bay Province, Papua New Guinea</address>
    </footer>
  </article>
</body>
</html>
```